Brookhaven Kitchens Stationary
Stationary Set with Business Card
Project: Brookhaven Kitchens Stationary
Brookhaven Kitchens Stationary - Chef / Catering
Creative Brief
Professional
Daniel Hensley
Chef/Owner
4738 W. Marlow Ave Orlando, FL 32899
dan@brookhavenkitchens.example
www.brookhavenkitchens.example
Simple with the BK (circle) part of the logo on the back, like a branding iron

```html
<!DOCTYPE html>
<html lang="en">
<head>
<meta charset="utf-8">
<title>Brookhaven Kitchens – Business Card</title>
<link rel="stylesheet" href="https://fonts.googleapis.com/css2?family=Open+Sans:wght@400;600;700&display=swap">
<style>
  :root {
    --page-bg: #e7e3de;
    --card-dark: #3e3e40;
    --band-rust: #c1603d;
    --band-rust-deep: #a94f31;
    --band-edge: #d98a66;
    --cream: #efe6d6;
    --text-soft: #d6d0c6;
    --accent: #d06a43;
    --mark-faint: rgba(255, 255, 255, 0.07);
  }
  * { box-sizing: border-box; margin: 0; padding: 0; }
  html, body {
    width: 1200px;
    height: 780px;
    overflow: hidden;
    background: var(--page-bg);
    font-family: "Open Sans", Arial, sans-serif;
  }
  .business-card {
    position: absolute;
    left: 75px;
    top: 90px;
    width: 1050px;
    height: 600px;
    border-radius: 34px;
    background: var(--card-dark);
    overflow: hidden;
    box-shadow: 0 14px 34px rgba(0, 0, 0, 0.25);
  }
  .header-band {
    position: absolute;
    left: 0; top: 0;
    width: 100%;
    height: 200px;
    background:
      repeating-linear-gradient(90deg, rgba(0,0,0,0.04) 0 2px, transparent 2px 5px),
      linear-gradient(180deg, var(--band-rust), var(--band-rust-deep));
    border-bottom: 4px solid var(--band-edge);
  }
  .owner {
    position: absolute;
    right: 62px;
    top: 62px;
    text-align: right;
    color: var(--cream);
  }
  .owner-name { font-size: 31px; font-weight: 700; letter-spacing: 0.3px; }
  .owner-title { font-size: 19px; font-weight: 400; margin-top: 4px; }
  .brand-circle {
    position: absolute;
    left: 70px;
    top: 140px;
    width: 124px;
    height: 124px;
    border-radius: 50%;
    background: var(--card-dark);
    border: 6px solid var(--cream);
  }
  .brand-name {
    position: absolute;
    left: 62px;
    top: 282px;
    font-size: 38px;
    font-weight: 600;
    color: var(--cream);
    letter-spacing: 0.2px;
  }
  .address {
    position: absolute;
    left: 62px;
    top: 352px;
    font-size: 19px;
    line-height: 1.35;
    color: var(--text-soft);
  }
  .contact-list {
    position: absolute;
    left: 62px;
    top: 452px;
    list-style: none;
  }
  .contact-list li {
    display: flex;
    align-items: center;
    gap: 14px;
    font-size: 19px;
    color: var(--text-soft);
    height: 36px;
  }
  .contact-list svg { width: 20px; height: 20px; flex: none; }
  .faint-mark {
    position: absolute;
    left: 640px;
    top: 205px;
    width: 300px;
    height: 300px;
    border-radius: 50%;
    border: 16px solid var(--mark-faint);
  }
</style>
</head>
<body>
  <main class="business-card">
    <div class="header-band"></div>

    <div class="owner">
      <div class="owner-name">Daniel Hensley</div>
      <div class="owner-title">Chef/Owner</div>
    </div>

    <div class="brand-circle"></div>
    <div class="brand-name">Brookhaven Kitchens</div>

    <div class="faint-mark"></div>

    <address class="address" style="font-style: normal;">
      4738 W. Marlow Ave<br>
      Orlando, FL 32899
    </address>

    <ul class="contact-list">
      <li>
        <svg viewBox="0 0 20 20" aria-hidden="true">
          <path fill="var(--accent)" d="M5 2l3 4-2 2c1 2 3 4 5 5l2-2 4 3-2 3C9 17 3 11 2 4z"/>
        </svg>
        407-555-0186
      </li>
      <li>
        <svg viewBox="0 0 20 20" aria-hidden="true">
          <circle cx="10" cy="10" r="8" fill="none" stroke="var(--accent)" stroke-width="2.4"/>
          <circle cx="10" cy="10" r="3" fill="none" stroke="var(--accent)" stroke-width="2.4"/>
        </svg>
        dan@brookhavenkitchens.example
      </li>
      <li>
        <svg viewBox="0 0 20 20" aria-hidden="true">
          <circle cx="10" cy="10" r="8" fill="none" stroke="var(--accent)" stroke-width="2"/>
          <ellipse cx="10" cy="10" rx="3.5" ry="8" fill="none" stroke="var(--accent)" stroke-width="1.6"/>
          <line x1="2" y1="10" x2="18" y2="10" stroke="var(--accent)" stroke-width="1.6"/>
        </svg>
        www.brookhavenkitchens.example
      </li>
    </ul>
  </main>
</body>
</html>
```